Digital Marketing Online Shop Needs a Home Page Web Design

Here is some background on the new home page and the message we want to relay to people visiting our site.
The new site design will be very similar to the following sites
http://plivora.com/
https://quillmarsh.com/
http://barelytidy.io/
http://craftturnip.com/
http://clipmelon.com/
We are a small marketing agency of 3 and we have built up and impressive contact list of partners over the last 16 years to help our customers take their digital marketing to the next level.
The four core areas of products we will be promoting and selling through our online shop are the following :
Web design
Content marketing
Graphic design
Coaching
We operate our agency in a new way, not the old school way so our customers can receive on-demand marketing.
We plan to have an online shop so visitors can purchase some of our services, very similar to how Quill Marshing and Craft Turnip offer their services.
In the end, we want the same call to action layout as Plivora, Quill Marsh and Craft Turnip, however, since we are an agency we would like to blend in Barely Tidy's layout.
We want the customer to either contact us about our services or purchase one of the services from our shop.
We are trying to make the whole digital marketing experience more transactional like retail and not so traditional servicey. :-)
It is from our years of experience and finding the right partners that allows us to offer this type of solution to businesses in the Maritime Provinces (New Brunswick, Nova Scotia, Prince Edward Island, Canada).
Also, because we are offering more of an on-demand/self serve option and we have lower overhead, we hope to pass along great pricing to our customers for their marketing needs. We really want this offer to expand outside of our local market in Saint John, New Brunswick.
I would also like to have a call to action written for a hero image at the top of the page, like the Plivora site.
After that I would like the content to flow through similar to Quill Marsh & Plivora. But mix in some of the agency like content you see with Clipmelon, Barely Tidy.
I have also included the first draft of the content for our home page.
Menu Items will be About, How We Work, Learn, Shop, Contact
Please let me know if you need anything else.
Small businesses, 1-10 person companies with up to 5 million in revenue. Mostly service companies, but some retail.
Marketing
1 page

```html
<!DOCTYPE html>
<html lang="en">
<head>
<meta charset="utf-8">
<title>Kelpway Studio — Digital Marketing Company</title>
<link href="https://fonts.googleapis.com/css2?family=Open+Sans:wght@400;600;700&family=Roboto:wght@400;500&display=swap" rel="stylesheet">
<style>
:root{
  --blue:#1f6fc1;
  --blue-dark:#1a5ea6;
  --orange:#f47b13;
  --ink:#222;
  --body:#555;
  --muted:#888;
  --panel:#f2f6fa;
  --client-bg:#edf1f5;
  --line:#d9dde2;
  --white:#fff;
}
*{box-sizing:border-box;margin:0;padding:0}
html,body{width:1200px;height:2866px;overflow:hidden}
body{position:relative;background:var(--white);font-family:"Roboto",Arial,sans-serif;color:var(--body)}
.abs{position:absolute}
h1,h2,h3{font-family:"Open Sans",Arial,sans-serif;color:var(--ink)}
.section-title{position:absolute;left:0;width:1200px;text-align:center;font-size:27px;font-weight:700;letter-spacing:.5px}
.section-lead{position:absolute;left:250px;width:700px;text-align:center;font-size:14.5px;line-height:21px;color:var(--body)}
.btn{position:absolute;display:flex;align-items:center;justify-content:center;color:var(--white);font-family:"Open Sans",Arial,sans-serif;font-weight:600;text-transform:uppercase;font-size:13px;letter-spacing:.4px;background:var(--blue)}

/* header */
.site-header{position:absolute;top:0;left:0;width:1200px;height:95px;background:var(--white)}
.brand{position:absolute;left:74px;top:26px;display:flex;align-items:center;gap:10px}
.brand-mark{width:40px;height:40px;border-radius:50%;background:var(--blue)}
.brand-name{font-family:"Open Sans",sans-serif;font-weight:700;font-size:22px;color:#2a2a2a;line-height:24px}
.brand-tag{font-size:9px;letter-spacing:.5px;color:var(--muted);text-transform:uppercase}
.main-nav{position:absolute;top:44px;right:72px;display:flex;gap:46px;font-family:"Open Sans",sans-serif;font-size:13px;color:#333;text-transform:uppercase}
.main-nav .active{color:var(--blue);position:relative}
.main-nav .active::after{content:"";position:absolute;left:0;right:0;top:30px;height:3px;background:var(--blue)}

/* hero */
.hero{position:absolute;top:95px;left:0;width:1200px;height:526px;background:linear-gradient(110deg,#3a3d41 0%,#5b5d60 40%,#4a3b3c 70%,#3d3f44 100%)}
.hero-title{position:absolute;top:185px;left:0;width:1200px;text-align:center;color:var(--white);font-size:38px;font-weight:700;letter-spacing:.5px}
.hero-text{position:absolute;top:252px;left:230px;width:740px;text-align:center;color:#f0f0f0;font-size:15px;line-height:25px}
.hero .btn{background:var(--orange)}

/* services */
.service{position:absolute;top:805px;width:340px;text-align:center}
.service-icon{width:122px;height:122px;margin:0 auto;border-radius:50%;border:1px solid #e6e9ec;display:flex;align-items:center;justify-content:center}
.service-name{margin-top:22px;font-family:"Roboto",sans-serif;font-weight:500;font-size:19px;color:var(--ink)}
.service-text{margin:10px auto 0;width:280px;font-size:12.5px;line-height:18px;color:var(--body)}
.service .btn{position:static;margin:24px auto 0;width:115px;height:31px;font-size:12px}

/* how we work */
.video{position:absolute;top:1127px;left:0;width:579px;height:440px;background:linear-gradient(160deg,#8a8e90 0%,#55595c 55%,#2b2e31 100%)}
.play{position:absolute;left:246px;top:178px}
.how{position:absolute;top:1127px;left:579px;width:621px;height:440px;background:var(--panel)}
.how h2{position:absolute;left:57px;top:70px;font-size:27px;font-weight:700}
.how p{position:absolute;left:57px;width:487px;font-size:13px;line-height:23px;text-align:justify;color:var(--body)}

/* team */
.member{position:absolute;top:1745px;width:230px;text-align:center}
.avatar{width:220px;height:220px;margin:0 auto;border-radius:50%;border:1px solid #e3e6e9;padding:5px}
.avatar div{width:100%;height:100%;border-radius:50%;background:linear-gradient(180deg,#e9ecef,#c9ced3)}
.member-name{margin-top:20px;font-size:21px;color:var(--ink)}
.member-role{margin-top:2px;font-size:15px;color:var(--blue)}
.member-rule{width:150px;height:1px;background:var(--line);margin:10px auto 0}
.member-links{margin-top:11px;display:flex;justify-content:center;gap:10px}
.member-links span{width:11px;height:11px;border-radius:50%;background:#999}

/* clients */
.clients{position:absolute;top:2142px;left:0;width:1200px;height:264px;background:var(--client-bg)}
.client{position:absolute;top:110px;display:flex;align-items:center;gap:8px;font-family:"Open Sans",sans-serif;font-weight:600;font-size:24px;color:#555}
.client i{width:20px;height:20px;border-radius:50%;background:#8a8a8a;display:block}
.clients-panel{position:absolute;left:705px;top:0;width:495px;height:264px;background:var(--blue)}
.clients-panel h2{position:absolute;left:38px;top:60px;color:var(--white);font-size:27px;line-height:34px;font-weight:700}
.arrow{position:absolute;top:166px;width:40px;height:40px;display:flex;align-items:center;justify-content:center}

/* contact */
.contact{position:absolute;top:2406px;left:0;width:1200px;height:365px}
.map{position:absolute;left:100px;top:30px;width:1000px;height:300px;background:radial-gradient(ellipse at center,#eef2f6 0%,#f7f9fb 60%,var(--white) 100%)}
.field{position:absolute;border:1px solid #cfd4d9;border-radius:3px;background:var(--white);display:flex;align-items:center;gap:8px;padding-left:16px;font-size:13px;color:#999}
.field svg{flex:none}

/* footer */
.site-footer{position:absolute;top:2771px;left:0;width:1200px;height:95px;background:var(--blue)}
.copyright{position:absolute;left:76px;top:38px;color:var(--white);font-size:12.5px}
.social{position:absolute;top:33px;width:29px;height:29px;border-radius:50%;background:var(--white)}
</style>
</head>
<body>

<header class="site-header">
  <div class="brand">
    <div class="brand-mark"></div>
    <div>
      <div class="brand-name">Kelpway Studio</div>
      <div class="brand-tag">Plan | Build | Grow Online</div>
    </div>
  </div>
  <nav class="main-nav">
    <span class="active">Home</span><span>About</span><span>How We Work</span><span>Learn</span><span>Shop</span><span>Contact</span>
  </nav>
</header>

<section class="hero" role="img" aria-label="Hero photo: a man in a red sweater holding a tablet beside an awards stand in a bright office">
  <svg class="abs" style="left:58px;top:205px" width="28" height="60" viewBox="0 0 28 60"><path d="M26 2 2 30l24 28" fill="none" stroke="#fff" stroke-width="2.5" opacity=".8"/></svg>
  <svg class="abs" style="left:1114px;top:205px" width="28" height="60" viewBox="0 0 28 60"><path d="M2 2l24 28L2 58" fill="none" stroke="#fff" stroke-width="2.5" opacity=".8"/></svg>
  <h1 class="hero-title">DIGITAL MARKETING COMPANY</h1>
  <p class="hero-text">At vero eos et accusamus et iusto odio dignissimos ducimus qui blanditiis praesentium voluptatum del eniti atque corrupti quos dolores et quas molestias</p>
  <span class="btn" style="left:525px;top:321px;width:150px;height:43px;font-size:14px">Learn More</span>
</section>

<h2 class="section-title" style="top:683px">OUR SERVICES</h2>
<p class="section-lead" style="top:733px">At vero eos et accusamus et iusto odio dignissimos ducimus qui blanditiis praesentium voluptatum deleniti atque corrupti quos dolores et quas molestias</p>

<div class="service" style="left:75px">
  <div class="service-icon"><svg width="52" height="52" viewBox="0 0 52 52"><path d="M8 44l3-12 24-24 9 9-24 24z" fill="var(--blue)"/><path d="M33 10l9 9" stroke="#fff" stroke-width="2"/><path d="M8 44l3-12 9 9z" fill="#fff" opacity=".35"/></svg></div>
  <div class="service-name">CONTENT MARKETING</div>
  <p class="service-text">Content Marketing is the 21st century what traditional advertising was to the '60s.</p>
  <span class="btn">Purchase</span>
</div>
<div class="service" style="left:432px">
  <div class="service-icon"><svg width="60" height="48" viewBox="0 0 60 48"><rect x="8" y="5" width="44" height="30" rx="2" fill="none" stroke="var(--blue)" stroke-width="4"/><path d="M2 40h56l-4 5H6z" fill="var(--blue)"/></svg></div>
  <div class="service-name">WEB DESIGN</div>
  <p class="service-text">Let's be honest: Your website is the face of your business in the modern world.</p>
  <span class="btn">Purchase</span>
</div>
<div class="service" style="left:789px">
  <div class="service-icon"><svg width="56" height="56" viewBox="0 0 56 56"><path d="M48 4c3 1 4 4 2 6L32 30l-6-6L42 5c2-2 4-2 6-1z" fill="var(--blue)"/><path d="M22 28l6 6c-2 10-10 16-22 14 6-4 4-10 8-15 2-3 5-5 8-5z" fill="var(--blue)"/></svg></div>
  <div class="service-name">GRAPHIC DESIGN</div>
  <p class="service-text">Creating a consistent and eye-catching brand for your business is one of the best ways</p>
  <span class="btn">Purchase</span>
</div>

<div class="video" role="img" aria-label="Video still: people walking through a glass-walled office lobby">
  <svg class="play" width="86" height="64" viewBox="0 0 86 64"><circle cx="43" cy="32" r="31" fill="#fff" opacity=".9"/><path d="M35 18l24 14-24 14z" fill="#333"/></svg>
</div>
<section class="how">
  <h2>HOW WE WORK</h2>
  <p style="top:124px">Sed ut perspiciatis unde omnis iste natus error sit voluptatem accusantium doloremque laudantium, totam rem aperiam, eaque ipsa.</p>
  <p style="top:188px">Nemo enim ipsam voluptatem quia voluptas sit aspernatur aut odit aut fugit, sed quia consequuntur magni dolores eos qui ratione voluptatem sequi nesciunt Neque porro quisquam est, qui dolorem ipsum quia dolor sit amet, consectetur adipisci velit, sed quia non numquam eius</p>
  <span class="btn" style="left:57px;top:320px;width:144px;height:40px">Learn More</span>
</section>

<h2 class="section-title" style="top:1629px">MEET OUR TEAM</h2>
<p class="section-lead" style="top:1679px">At vero eos et accusamus et iusto odio dignissimos ducimus qui blanditiis praesentium voluptatum deleniti atque corrupti quos dolores et quas molestias</p>

<div class="member" style="left:82px">
  <div class="avatar"><div role="img" aria-label="Portrait photo of a team member"></div></div>
  <div class="member-name">Owen Hartle</div><div class="member-role">Founder &amp; CEO</div>
  <div class="member-rule"></div><div class="member-links"><span></span><span></span><span></span></div>
</div>
<div class="member" style="left:351px">
  <div class="avatar"><div role="img" aria-label="Portrait photo of a team member"></div></div>
  <div class="member-name">Clara Benning</div><div class="member-role">Founder &amp; CEO</div>
  <div class="member-rule"></div><div class="member-links"><span></span><span></span><span></span></div>
</div>
<div class="member" style="left:619px">
  <div class="avatar"><div role="img" aria-label="Portrait photo of a team member"></div></div>
  <div class="member-name">Miles Ardent</div><div class="member-role">Founder &amp; CEO</div>
  <div class="member-rule"></div><div class="member-links"><span></span><span></span><span></span></div>
</div>
<div class="member" style="left:888px">
  <div class="avatar"><div role="img" aria-label="Portrait photo of a team member"></div></div>
  <div class="member-name">Theo Lanfield</div><div class="member-role">Founder &amp; CEO</div>
  <div class="member-rule"></div><div class="member-links"><span></span><span></span><span></span></div>
</div>

<section class="clients">
  <div class="client" style="left:72px"><i></i>Harbourline</div>
  <div class="client" style="left:305px">Tidewater Co</div>
  <div class="client" style="left:510px">Northcove</div>
  <div class="clients-panel">
    <h2>MEET<br>OUR CLIENTS</h2>
    <div class="arrow" style="left:40px;background:#2b2f35"><svg width="10" height="14" viewBox="0 0 10 14"><path d="M8 1L2 7l6 6" fill="none" stroke="#fff" stroke-width="2"/></svg></div>
    <div class="arrow" style="left:81px;background:var(--blue-dark)"><svg width="10" height="14" viewBox="0 0 10 14"><path d="M2 1l6 6-6 6" fill="none" stroke="#fff" stroke-width="2"/></svg></div>
  </div>
</section>

<section class="contact">
  <div class="map" role="img" aria-label="Faint dotted world map in the background"></div>
  <h2 class="section-title" style="top:72px">GET IN TOUCH</h2>
  <div class="field" style="left:254px;top:141px;width:335px;height:42px"><svg width="11" height="12" viewBox="0 0 11 12"><circle cx="5.5" cy="3.5" r="3" fill="#555"/><path d="M0 12c0-4 2.5-5.5 5.5-5.5S11 8 11 12z" fill="#555"/></svg>Name</div>
  <div class="field" style="left:608px;top:141px;width:334px;height:42px"><svg width="13" height="10" viewBox="0 0 13 10"><rect width="13" height="10" fill="#555"/><path d="M0 0l6.5 5L13 0" fill="none" stroke="#fff"/></svg>Email</div>
  <div class="field" style="left:254px;top:202px;width:688px;height:58px;align-items:flex-start;padding-top:12px"><svg width="13" height="12" viewBox="0 0 13 12"><ellipse cx="6.5" cy="5" rx="5.5" ry="4.2" fill="none" stroke="#555" stroke-width="1.3"/><path d="M3 8l-1 3 3-2" fill="#555"/></svg>Message</div>
  <span class="btn" style="left:803px;top:279px;width:137px;height:42px;font-size:14px">Submit</span>
</section>

<footer class="site-footer">
  <p class="copyright">Copyright © 2016 Kelpway Studio. All Right Reserved.</p>
  <span class="social" style="left:939px" aria-label="Social link"></span>
  <span class="social" style="left:978px" aria-label="Social link"></span>
  <span class="social" style="left:1017px" aria-label="Social link"></span>
  <span class="social" style="left:1056px" aria-label="Social link"></span>
  <span class="social" style="left:1095px" aria-label="Social link"></span>
</footer>

</body>
</html>
```